Business Consulting Business Card

professional business card with basic information (1) First and Last name (2) email address, (3) phone number, (4) website.

```html
<!DOCTYPE html>
<html lang="en">
<head>
<meta charset="utf-8">
<title>Bay Linden — Business Card</title>
<link href="https://fonts.googleapis.com/css2?family=Montserrat:wght@400&family=Roboto:wght@300;400;500&display=swap" rel="stylesheet">
<style>
  :root {
    --bg: #2c2c2e;
    --teal-start: #4fadc8;
    --teal-end: #50c0be;
    --teal: #4db8c4;
    --navy: #0f2a3d;
    --paper: #f6f6f6;
    --ink: #333333;
    --white: #ffffff;
  }
  * { margin: 0; padding: 0; box-sizing: border-box; }
  html, body {
    width: 1044px; height: 1200px; overflow: hidden;
    background: var(--bg);
  }
  .canvas { position: relative; width: 1044px; height: 1200px; }
  .card {
    position: absolute; left: 196px; width: 630px; height: 360px;
  }
  .card--front {
    top: 195px;
    background: linear-gradient(100deg, var(--teal-start), var(--teal-end));
  }
  .card--back { top: 645px; background: var(--paper); }

  .brand-mark { position: absolute; border-radius: 50%; }
  .brand-name {
    position: absolute; white-space: nowrap; line-height: 1;
    font-family: 'Montserrat', sans-serif; font-weight: 400;
    letter-spacing: 0.26em;
  }
  .card--front .brand-mark {
    left: 109px; top: 136px; width: 70px; height: 88px;
    background: var(--white); border-radius: 50%;
  }
  .card--front .brand-mark { width: 78px; height: 78px; top: 141px; left: 114px; }
  .card--front .brand-name {
    left: 212px; top: 164px; font-size: 38px; color: var(--white);
  }
  .card--back .brand-mark {
    left: 158px; top: 56px; width: 62px; height: 62px; background: var(--teal);
  }
  .card--back .brand-name {
    left: 232px; top: 72px; font-size: 31px; color: var(--navy);
  }

  .person {
    position: absolute; right: 375px; top: 250px; text-align: right;
    font-family: 'Roboto', sans-serif; line-height: 1;
  }
  .person__name { font-size: 23px; font-weight: 500; color: var(--teal); }
  .person__role { font-size: 17px; font-weight: 300; color: var(--ink); margin-top: 2px; }

  .divider {
    position: absolute; left: 314px; top: 240px; width: 2px; height: 60px;
    background: var(--teal);
  }

  .contacts {
    position: absolute; left: 374px; top: 239px; list-style: none;
    font-family: 'Roboto', sans-serif; font-weight: 300; font-size: 18px; color: var(--ink);
  }
  .contacts li { display: flex; align-items: center; height: 23px; }
  .contacts svg { width: 14px; height: 14px; margin-right: 12px; flex: none; }
</style>
</head>
<body>
<div class="canvas">
  <section class="card card--front">
    <span class="brand-mark" aria-hidden="true"></span>
    <span class="brand-name">BAY LINDEN</span>
  </section>

  <section class="card card--back">
    <span class="brand-mark" aria-hidden="true"></span>
    <span class="brand-name">BAY LINDEN</span>

    <div class="person">
      <div class="person__name">MARLA QUINT</div>
      <div class="person__role">President</div>
    </div>

    <span class="divider" aria-hidden="true"></span>

    <ul class="contacts">
      <li>
        <svg viewBox="0 0 14 14" fill="none" stroke="var(--teal)" stroke-width="1.2"><rect x="3.5" y="0.8" width="7" height="12.4" rx="1.2"/><line x1="6" y1="11" x2="8" y2="11"/></svg>
        (555) 201 - 0148
      </li>
      <li>
        <svg viewBox="0 0 14 14"><rect x="1" y="3" width="12" height="8" fill="var(--teal)"/><polyline points="1,3 7,8 13,3" fill="none" stroke="var(--paper)" stroke-width="1"/></svg>
        hello@baylinden.com
      </li>
      <li>
        <svg viewBox="0 0 14 14" fill="none" stroke="var(--teal)" stroke-width="1"><circle cx="7" cy="7" r="5.8"/><ellipse cx="7" cy="7" rx="2.6" ry="5.8"/><line x1="1.2" y1="7" x2="12.8" y2="7"/><line x1="2" y1="4" x2="12" y2="4"/><line x1="2" y1="10" x2="12" y2="10"/></svg>
        www.baylinden.com
      </li>
    </ul>
  </section>
</div>
</body>
</html>
```